website re-design - the brisk loft

The Brisk Loft is an existing website that we built using a new zealand based online CMS tool which is quite flexible and accomodates custom designs. You can check it here: http://www.pagecrafter.co.nz/.

We have a logo already and the content on the website is OK.
The website can be found at www.thebriskloft.com.au

mainly the homepage, but if the design is easily adapted to the other pages then, we will commission the winner to update these pages also.
Updates

Hi there,  I am uploading an image to be used as the main image on the homepage design,  so all submissions have the same image.

Target Market(s)

property developers, architects, builders, home buyers

Industry/Entity Type

Shop

Requirements
Must have
• Must utilise the existing CMS or at least be compatible to upload
Nice to have
• a promotional banner that can be turned off and on and changed as required as we offer different promotions over time.

```html
<!DOCTYPE html>
<html lang="en">
<head>
<meta charset="utf-8">
<title>The Brisk Loft – Get a Quote</title>
<link rel="stylesheet" href="https://fonts.googleapis.com/css2?family=Open+Sans:wght@400;600;700&family=Ubuntu:wght@400;500&display=swap">
<style>
:root{
  --bg:#f5e4c6;
  --page:#ffffff;
  --orange:#f18a1c;
  --heading:#1d3210;
  --text:#4a4a4a;
  --nav-text:#f59a2a;
  --offer-bg:#f6eedd;
  --offer-red:#a40d0d;
  --field-border:#c9c9c9;
  --rule:#cfcfcf;
  --social:#3b5998;
}
*{box-sizing:border-box;margin:0;padding:0}
html,body{width:1152px;height:1200px;overflow:hidden}
body{background:var(--bg);font-family:"Open Sans",Arial,sans-serif;color:var(--text);position:relative}
.page{position:absolute;left:86px;top:0;width:978px;height:1154px;background:var(--page);box-shadow:0 0 6px rgba(0,0,0,.25)}
.header{position:absolute;left:0;top:0;width:978px;height:112px;box-shadow:0 6px 8px -6px rgba(0,0,0,.25)}
.brand-mark{position:absolute;left:63px;top:20px;width:66px;height:66px;background:var(--orange)}
.brand-name{position:absolute;left:196px;top:38px;font-family:"Ubuntu",sans-serif;font-size:25px;color:#555;line-height:1;white-space:nowrap}
.brand-tag{position:absolute;left:196px;top:63px;font-family:"Ubuntu",sans-serif;font-size:11.5px;color:var(--orange);letter-spacing:.4px;white-space:nowrap}
.contact{position:absolute;left:788px;top:18px;font-size:13px;line-height:17.5px;color:#555}
.contact .phone{color:var(--orange);font-weight:700;font-size:14.5px;margin-bottom:5px}
.nav{position:absolute;left:79px;top:141px;list-style:none}
.nav li{width:184px;height:32px;margin-bottom:4.5px;background:linear-gradient(#3a3a3a,#0c0c0c 60%,#1a1a1a);box-shadow:1px 2px 3px rgba(0,0,0,.4);color:var(--nav-text);font-size:15.5px;line-height:32px;padding-left:38px}
.nav li.active{background:linear-gradient(#ffc05a,#f7931e);color:#3a2a10}
.offer{position:absolute;left:85px;top:401px;width:177px;height:333px;background:var(--offer-bg)}
.offer-title{position:absolute;left:33px;top:9px;font-size:17px;font-weight:700;color:var(--offer-red)}
.offer-sub{position:absolute;left:33px;top:32px;font-size:12px;font-weight:600;color:#333}
.offer-photo{position:absolute;left:0;top:52px;width:177px;height:133px;background:linear-gradient(160deg,#d9dde0,#a7b0b4 55%,#6d7478)}
.offer-badge{position:absolute;left:115px;top:151px;width:61px;height:61px;border-radius:50%;background:#b10c0c;color:#fff;font-weight:700;text-align:center;font-size:19px;line-height:20px;padding-top:11px}
.offer-badge small{display:block;font-size:14px}
.offer-name{position:absolute;left:16px;top:196px;font-size:14px;font-weight:700;color:#e0701a;line-height:17px}
.offer-desc{position:absolute;left:16px;top:237px;width:152px;font-size:11.5px;line-height:17px;color:#333}
.offer-was{position:absolute;right:14px;top:294px;font-size:9.5px;text-decoration:line-through;color:#555;font-weight:700}
.offer-price{position:absolute;right:14px;top:305px;font-size:14px;font-weight:700;color:var(--offer-red)}
.intro{position:absolute;left:306px;top:144px;width:712px;font-size:13px;line-height:17.5px;color:var(--orange)}
.q{position:absolute;left:308px;font-size:16px;font-weight:700;color:var(--heading);line-height:20px}
.opt{position:absolute;left:308px;font-size:12.8px;line-height:18px;color:#555;display:flex;align-items:center;gap:8px}
.opt::before{content:"";width:11px;height:11px;border:1px solid #999;background:linear-gradient(#eee,#fff)}
.select{position:absolute;left:308px;top:225px;width:140px;height:19px;border:1px solid #bbb;font-size:11.5px;line-height:17px;padding-left:4px;color:#222;font-family:monospace}
.select::after{content:"";position:absolute;right:1px;top:1px;width:15px;height:15px;border:1px solid #777;background:#e9e9e9}
.select i{position:absolute;right:5px;top:7px;border:4px solid transparent;border-top-color:#000;z-index:1}
.file{position:absolute;left:309px;width:147px;height:22px;border:1px solid #999;border-top-color:#666;border-left-color:#666}
.browse{position:absolute;left:458px;width:74px;height:21px;border:1px solid #999;border-radius:2px;background:linear-gradient(#fafafa,#ddd);font-family:monospace;font-size:11px;line-height:19px;text-align:center;color:#222}
.field{position:absolute;left:308px;width:314px;height:24px;border:1px solid var(--field-border);font-size:13px;color:#666;padding-left:7px;line-height:22px}
.send{position:absolute;left:307px;top:1067px;width:65px;height:25px;border-radius:4px;background:linear-gradient(#ffc45d,#f7931e);color:#4a2c08;font-weight:700;font-size:14px;text-align:center;line-height:25px}
.rule{position:absolute;left:296px;top:1109px;width:768px;height:1px;background:var(--rule)}
.share{position:absolute;top:1123px;height:18px;border:1px solid #c8d3e4;border-radius:2px;background:#eef2f8;font-size:11px;line-height:16px;color:var(--social);text-align:center}
.follow{position:absolute;left:950px;top:1126px;font-size:11.5px;color:#666}
.follow-box{position:absolute;left:1025px;top:1121px;width:23px;height:23px;background:var(--social);border-radius:3px}
.footer-links{position:absolute;left:88px;top:1168px;font-size:13.5px;color:#333}
.copyright{position:absolute;right:103px;top:1168px;font-size:13.5px;color:#555}
</style>
</head>
<body>
<div class="page">
  <header class="header">
    <div class="brand-mark"></div>
    <div class="brand-name">The Brisk Loft</div>
    <div class="brand-tag">ARCHITECTURAL SCALE MODELS</div>
    <div class="contact">
      <div class="phone">Phone: (08) 7340 5582</div>
      48 Harbourview Rd<br>Kelmscott, WA 6111<br>Australia
    </div>
  </header>
</div>

<ul class="nav">
  <li>Home</li>
  <li class="active">Gallery</li>
  <li>Order Online</li>
  <li>Get a Quote</li>
  <li>3D Visualization</li>
  <li>Contact</li>
  <li>About Us</li>
</ul>

<aside class="offer">
  <div class="offer-title">Special Offer</div>
  <div class="offer-sub">for a limited time!</div>
  <div class="offer-photo" role="img" aria-label="Photo of a white architectural scale model of a two-storey house"></div>
  <div class="offer-badge">50%<small>Off</small></div>
  <div class="offer-name">Integer Porta<br>Dignissim Augue</div>
  <div class="offer-desc">Facilisis ridiculus adipiscing porttitor, sit arcu parturient a! Habitasse!</div>
  <div class="offer-was">$ 000.00</div>
  <div class="offer-price">$ 000.00</div>
</aside>

<p class="intro">To get a quote for your model, please fill in what you can here and upload a PDF or .dwg file of your project.&nbsp; We will get back to you with a quotation within 24 hours.&nbsp; Alternatively, please call us on 041 7 302 664.</p>

<div class="q" style="top:195px">What scale do you need?</div>
<div class="select">1:100<i></i></div>

<div class="q" style="top:258px">How much colour do you need in the model?</div>
<div class="opt" style="top:285px">Generic white</div>
<div class="opt" style="top:307px">Some colour/material change to highlight elements</div>
<div class="opt" style="top:329px">Full colour</div>

<div class="q" style="top:360px">Acrylic display case required?</div>
<div class="opt" style="top:386px">Yes</div>
<div class="opt" style="top:408px">No</div>

<div class="q" style="top:440px">When do you need the model?</div>
<div class="opt" style="top:466px">Whatever timeframe we are currently working to</div>
<div class="opt" style="top:488px">Within the next 6 weeks</div>
<div class="opt" style="top:510px">I would prefer a better price than a fast delivery</div>
<div class="opt" style="top:533px">It is urgent</div>
<div class="opt" style="top:555px">I have an absolute deadline</div>
<div class="opt" style="top:577px">Other</div>

<div class="q" style="top:610px">Upload drawings here</div>
<div class="file" style="top:639px"></div><div class="browse" style="top:639px">Browse…</div>
<div class="file" style="top:669px"></div><div class="browse" style="top:669px">Browse…</div>
<div class="file" style="top:699px"></div><div class="browse" style="top:699px">Browse…</div>

<div class="q" style="top:737px">Notes</div>
<div class="field" style="top:761px">Insert any relevant notes here</div>

<div class="q" style="top:802px">Your Name *</div>
<div class="field" style="top:827px"></div>

<div class="q" style="top:857px">Phone</div>
<div class="field" style="top:881px"></div>

<div class="q" style="top:913px">Your Email *</div>
<div class="field" style="top:937px"></div>

<div class="q" style="top:968px">Comments</div>
<div class="field" style="top:993px;height:65px"></div>

<div class="send">Send</div>

<div class="rule"></div>
<div class="share" style="left:298px;width:31px">+1</div>
<div class="share" style="left:342px;width:40px">Like</div>
<div class="share" style="left:393px;width:52px">Share</div>
<div class="follow">Follow us</div>
<div class="follow-box"></div>

<div class="footer-links">Home | Gallery | Order | Quote | 3D | Contact | About</div>
<div class="copyright">© Copyright The Brisk Loft</div>
</body>
</html>
```